Corvale Spine & Joint Business Card

Need a business card using the logo provided. I want brand side of the card to be grey with the logo in the center of the card in white.

On the other side I leave to the designers

Target Market(s)

Personal Injury Attorneys

Industry/Entity Type

Medical

Contact Information for Business Card

Name, CEO. Cell Phone, (Hialeah, Address, Phone) (Homestead, Address, Phone) (Tallahassee, Address, Phone)

Colors

Designer to choose only greyscale colors for use in the design.

Requirements
Must have
• Logo by itself on one side

```html
<!DOCTYPE html>
<html lang="en">
<head>
<meta charset="UTF-8">
<title>Corvale Spine &amp; Joint Business Card</title>
<link href="https://fonts.googleapis.com/css2?family=Barlow:wght@400;500;600&display=swap" rel="stylesheet">
<style>
  :root {
    --page: #ffffff;
    --card-grey: #adadad;
    --card-white: #ffffff;
    --ink: #4b4b4b;
    --ink-soft: #9c9c9c;
    --icon: #8f8f8f;
    --shadow: rgba(0, 0, 0, 0.28);
  }
  * { box-sizing: border-box; margin: 0; padding: 0; }
  html, body {
    width: 1200px;
    height: 630px;
    overflow: hidden;
    background: var(--page);
    font-family: "Barlow", Arial, sans-serif;
  }
  .canvas {
    width: 1200px;
    height: 630px;
    display: flex;
    align-items: center;
    justify-content: center;
    gap: 44px;
  }
  .card {
    position: relative;
    width: 540px;
    height: 309px;
    box-shadow: 3px 4px 8px var(--shadow);
    overflow: hidden;
  }
  .card-front {
    background: var(--card-grey);
    display: flex;
    align-items: center;
    justify-content: center;
  }
  .brand {
    color: var(--card-white);
    font-weight: 500;
    text-align: center;
    line-height: 1;
  }
  .brand-name {
    display: block;
    font-size: 33px;
    letter-spacing: 6px;
    padding-left: 6px;
  }
  .brand-sub {
    display: block;
    margin-top: 6px;
    font-size: 15px;
    letter-spacing: 3px;
    padding-left: 3px;
  }
  .card-back { background: var(--card-white); }
  .back-panel {
    position: absolute;
    left: 0; top: 0;
    width: 212px;
    height: 100%;
    background: var(--card-grey);
    display: flex;
    align-items: flex-start;
    justify-content: center;
    padding-top: 80px;
  }
  .back-panel .brand-name { font-size: 24px; letter-spacing: 4.5px; padding-left: 4px; }
  .back-panel .brand-sub { font-size: 12px; letter-spacing: 2.5px; margin-top: 4px; }
  .spine-band {
    position: absolute;
    left: 212px; top: 0;
    width: 70px;
    height: 100%;
    background: linear-gradient(90deg, var(--card-grey) 0%, #d2d2d2 55%, var(--card-white) 100%);
  }
  .holder {
    position: absolute;
    left: 326px;
    top: 84px;
    color: var(--ink);
  }
  .holder-name {
    font-size: 23px;
    font-weight: 500;
    letter-spacing: 0.5px;
    line-height: 1;
  }
  .holder-role {
    margin-top: 6px;
    font-size: 16px;
    font-weight: 500;
    color: var(--ink-soft);
  }
  .contact {
    position: absolute;
    left: 326px;
    top: 184px;
    list-style: none;
    color: var(--ink);
    font-size: 15px;
    line-height: 1.35;
  }
  .contact li { display: flex; align-items: flex-start; gap: 6px; }
  .contact li + li { margin-top: 1px; }
  .contact .address { margin-top: 11px; }
  .contact svg { flex: none; margin-top: 3px; }
</style>
</head>
<body>
  <main class="canvas">
    <section class="card card-front" aria-label="Card front">
      <div class="brand">
        <span class="brand-name">CORVALE</span>
        <span class="brand-sub">SPINE &amp; JOINT</span>
      </div>
    </section>

    <section class="card card-back" aria-label="Card back">
      <div class="back-panel">
        <div class="brand">
          <span class="brand-name">CORVALE</span>
          <span class="brand-sub">SPINE &amp; JOINT</span>
        </div>
      </div>
      <div class="spine-band" role="img" aria-label="Spine silhouette illustration forming the edge between grey and white"></div>

      <div class="holder">
        <p class="holder-name">DANIEL REYES</p>
        <p class="holder-role">CEO</p>
      </div>

      <ul class="contact">
        <li>
          <svg width="10" height="15" viewBox="0 0 10 15" aria-hidden="true">
            <rect x="0.75" y="0.75" width="8.5" height="13.5" rx="1.5" fill="none" stroke="var(--icon)" stroke-width="1.2"/>
            <line x1="3.5" y1="12" x2="6.5" y2="12" stroke="var(--icon)" stroke-width="1"/>
          </svg>
          <span>+1 000-000-0000</span>
        </li>
        <li>
          <svg width="14" height="10" viewBox="0 0 14 10" aria-hidden="true">
            <rect x="0" y="0" width="14" height="10" fill="var(--icon)"/>
            <polyline points="0.5,0.8 7,5.5 13.5,0.8" fill="none" stroke="#ffffff" stroke-width="1"/>
          </svg>
          <span>daniel@corvale.com</span>
        </li>
        <li class="address">
          <svg width="11" height="15" viewBox="0 0 11 15" aria-hidden="true">
            <path d="M5.5 0.7C2.8 0.7 0.7 2.8 0.7 5.4c0 3.5 4.8 8.9 4.8 8.9s4.8-5.4 4.8-8.9C10.3 2.8 8.2 0.7 5.5 0.7z" fill="var(--icon)"/>
            <circle cx="5.5" cy="5.3" r="1.8" fill="#ffffff"/>
          </svg>
          <span>1234 Corvale Street<br>USA</span>
        </li>
      </ul>
    </section>
  </main>
</body>
</html>
```